Lantern Hill Publicity is a new boutique Press Office with a small roster of well-chosen clients across an array of disciplines; from Art and Technology to Restaurants and Fashion. Based in Greenpoint Brooklyn, Lantern Hill Publicity achieves outstanding results through hard work, tenacity, efficiency and a sense of humor. We need a simple, versatile and classic design. We would like each side of the card to be white text on a black background.

Boutique

```html
<!DOCTYPE html>
<html lang="en">
<head>
<meta charset="utf-8">
<title>Lantern Hill Publicity – Business Card</title>
<link href="https://fonts.googleapis.com/css2?family=Cinzel:wght@400;700&family=Roboto:wght@400&display=swap" rel="stylesheet">
<style>
  :root {
    --backdrop: #d9d6d1;
    --card: #0b0b0b;
    --ink: #ffffff;
    --ink-soft: #d8d8d8;
    --rule: #8a8a8a;
  }
  * { box-sizing: border-box; margin: 0; padding: 0; }
  html, body { width: 1200px; height: 900px; overflow: hidden; }
  body {
    background: var(--backdrop);
    display: flex;
    align-items: center;
    justify-content: center;
    gap: 40px;
    font-family: "Roboto", Arial, sans-serif;
    color: var(--ink);
  }
  .card {
    width: 540px;
    height: 309px;
    background: var(--card);
    position: relative;
    box-shadow: 0 10px 28px rgba(0,0,0,0.3);
  }

  /* Front */
  .card--front { display: flex; align-items: center; }
  .brand {
    width: 245px;
    display: flex;
    flex-direction: column;
    align-items: center;
    gap: 14px;
  }
  .brand__dot {
    width: 34px; height: 34px;
    border-radius: 50%;
    background: var(--ink);
  }
  .brand__name {
    font-family: "Cinzel", Georgia, serif;
    font-weight: 400;
    font-size: 15px;
    letter-spacing: 3px;
    text-align: center;
    line-height: 1.5;
    color: var(--ink);
  }
  .divider {
    width: 1px;
    height: 150px;
    background: var(--rule);
  }
  .details { padding-left: 30px; }
  .details__name {
    font-family: "Cinzel", Georgia, serif;
    font-weight: 700;
    font-size: 19px;
    letter-spacing: 1px;
  }
  .details__title {
    font-size: 10px;
    letter-spacing: 0.5px;
    color: var(--ink-soft);
    margin-bottom: 14px;
  }
  .contact { list-style: none; font-size: 11px; color: var(--ink-soft); }
  .contact li { display: flex; align-items: center; gap: 7px; margin-bottom: 5px; }
  .contact svg { width: 11px; height: 11px; flex: none; }
  .address { margin-top: 10px; font-size: 11px; line-height: 1.45; color: var(--ink-soft); }

  /* Back */
  .card--back {
    display: flex;
    flex-direction: column;
    align-items: center;
    justify-content: center;
    gap: 16px;
  }
  .card--back .brand__dot { width: 40px; height: 40px; }
  .card--back .brand__name { font-size: 17px; }
</style>
</head>
<body>

  <section class="card card--front">
    <div class="brand">
      <span class="brand__dot"></span>
      <p class="brand__name">LANTERN HILL<br>PUBLICITY</p>
    </div>
    <span class="divider"></span>
    <div class="details">
      <h1 class="details__name">MR. HARLOW</h1>
      <p class="details__title">DIRECTOR OPERATIONS</p>
      <ul class="contact">
        <li>
          <svg viewBox="0 0 11 11"><rect width="11" height="11" rx="1.5" fill="#9a9a9a"/><path d="M3 2.5c.5 2.8 2.5 4.9 5.5 5.5l.4-1.3-1.4-.6-.6.7C5.8 6.3 4.7 5.2 4.2 4.1l.7-.6-.6-1.4z" fill="#0b0b0b"/></svg>
          1718-5520-4417
        </li>
        <li>
          <svg viewBox="0 0 11 11"><rect width="11" height="11" rx="1.5" fill="#9a9a9a"/><rect x="3.5" y="2" width="4" height="7" rx="0.6" fill="#0b0b0b"/></svg>
          0347-2289-6630
        </li>
        <li>
          <svg viewBox="0 0 11 11"><rect width="11" height="11" rx="1.5" fill="#9a9a9a"/><rect x="2.2" y="3.2" width="6.6" height="4.6" fill="#0b0b0b"/><path d="M2.4 3.4l3.1 2.4 3.1-2.4" stroke="#9a9a9a" stroke-width="0.7" fill="none"/></svg>
          press@lanternhillpr.com
        </li>
      </ul>
      <p class="address">118 Franklin Street<br>Brooklyn 11222</p>
    </div>
  </section>

  <section class="card card--back">
    <span class="brand__dot"></span>
    <p class="brand__name">LANTERN HILL<br>PUBLICITY</p>
  </section>

</body>
</html>
```